Post Disaster Temporary Housing Literature Review poster

Wanting a poster design for two Emergency Management conferences we have coming up. The information to be included in the poster is capturing the purpose, findings and recommendations from a post disaster temporary housing literature review looking at “What should government consider in order to improve planning and decision making for accommodation needs after a disaster, and to support people’s transition to stable housing?”
I’d like to enhance the visual appeal through including relevant images or graphic. I am also open to reducing the text if needed.
The government group I work with focuses on the social and human side of disaster recovery so keen for any images to reflect the human aspect and not focus solely on disasters or housing.
Government and NGO's

```html
<!DOCTYPE html>
<html lang="en">
<head>
<meta charset="utf-8">
<title>Post Disaster Temporary Housing Literature Review</title>
<link href="https://fonts.googleapis.com/css2?family=Montserrat:wght@300;400;500;700;800&display=swap" rel="stylesheet">
<style>
  :root {
    --navy: #1a1d5e;
    --deep-blue: #1b3f9c;
    --blue: #1f6fd6;
    --sky: #2f9be0;
    --cyan: #2cb6e6;
    --ink: #141833;
    --page: #ececec;
    --white: #ffffff;
  }
  * { box-sizing: border-box; margin: 0; padding: 0; }
  html, body { width: 1200px; height: 1000px; overflow: hidden; }
  body {
    background: var(--page);
    font-family: "Montserrat", Arial, sans-serif;
    position: relative;
  }
  .poster {
    position: absolute;
    left: 269px; top: 32px;
    width: 662px; height: 936px;
    background: var(--white);
    overflow: hidden;
  }
  .header-art { position: absolute; left: 0; top: 0; width: 662px; height: 440px; }
  .brand {
    position: absolute; left: 42px; top: 38px;
    display: flex; align-items: center; gap: 12px;
  }
  .brand-square { width: 40px; height: 40px; background: var(--white); }
  .brand-name {
    color: var(--white); font-size: 12.5px; font-weight: 500; line-height: 18px;
  }
  .title { position: absolute; left: 42px; top: 343px; line-height: 1; }
  .title-strong { display: block; font-weight: 800; color: var(--navy); font-size: 25px; letter-spacing: 0.3px; }
  .title-light { display: block; font-weight: 400; color: var(--sky); font-size: 20px; margin: 6px 0 6px; letter-spacing: 0.3px; }
  .title-sub { display: block; font-weight: 800; color: var(--navy); font-size: 20px; letter-spacing: 0.3px; }
  .badge {
    position: absolute; color: var(--white); font-weight: 700;
    display: flex; align-items: center; justify-content: center;
  }
  .badge-purpose {
    left: 42px; top: 456px; width: 162px; height: 43px; font-size: 30px;
    background: linear-gradient(90deg, var(--sky), var(--deep-blue));
  }
  .purpose-text {
    position: absolute; left: 42px; top: 514px; width: 580px;
    font-size: 11.4px; line-height: 14.6px; color: var(--ink);
  }
  .badge-recommendations {
    left: 161px; top: 599px; width: 340px; height: 48px; font-size: 29px; border-radius: 6px;
    background: linear-gradient(90deg, var(--cyan), var(--navy));
  }
  .recommendation-list {
    position: absolute; left: 43px; top: 672px; width: 580px;
    list-style: none; display: grid; grid-template-columns: 300px 280px;
    grid-auto-rows: 45px; row-gap: 0;
  }
  .recommendation-list li {
    font-size: 20.5px; font-weight: 700; color: var(--navy); letter-spacing: 0.2px;
  }
  .footer-band {
    position: absolute; left: 0; top: 855px; width: 662px; height: 40px;
    background: linear-gradient(90deg, var(--blue), var(--navy));
    display: flex; align-items: center;
    color: var(--white); font-size: 13.5px; font-weight: 700;
  }
  .footer-notch { position: absolute; bottom: -6px; width: 14px; height: 8px; background: var(--white); }
  .contact { position: absolute; display: flex; align-items: center; gap: 8px; }
  .contact svg { width: 18px; height: 18px; }
</style>
</head>
<body>
<main class="poster">
  <svg class="header-art" viewBox="0 0 662 440" aria-hidden="true">
    <defs>
      <linearGradient id="panelGradient" x1="0" y1="0" x2="1" y2="0.4">
        <stop offset="0" stop-color="#1a1d5e"/>
        <stop offset="0.6" stop-color="#1b4fb0"/>
        <stop offset="1" stop-color="#1f8ad8"/>
      </linearGradient>
      <linearGradient id="photoGradient" x1="0" y1="0" x2="0" y2="1">
        <stop offset="0" stop-color="#6aa6e6"/>
        <stop offset="0.3" stop-color="#a9c2dc"/>
        <stop offset="0.55" stop-color="#b9b8b4"/>
        <stop offset="0.8" stop-color="#a08a6e"/>
        <stop offset="1" stop-color="#8e8a86"/>
      </linearGradient>
    </defs>
    <rect x="0" y="0" width="662" height="430" fill="url(#photoGradient)" role="img" aria-label="Photo of a row of newly built townhouses with red skip bins on the street"/>
    <path d="M0 0 H430 C410 60 370 80 300 92 C200 108 80 110 0 168 Z" fill="url(#panelGradient)"/>
    <path d="M430 0 C410 60 370 80 300 92 C200 108 80 110 0 168" fill="none" stroke="#ffffff" stroke-width="5"/>
    <path d="M0 300 C60 240 160 250 260 320 C340 380 420 430 520 410 C590 396 630 370 662 346 V440 H0 Z" fill="#ffffff"/>
    <path d="M0 308 C60 248 160 258 260 328 C340 388 420 438 520 418 C590 404 630 378 662 354" fill="none" stroke="#1f6fd6" stroke-width="6"/>
  </svg>

  <div class="brand">
    <span class="brand-square"></span>
    <span class="brand-name">Community Renewal<br>Advisory Network</span>
  </div>

  <h1 class="title">
    <span class="title-strong">POST DISASTER</span>
    <span class="title-light">TEMPORARY HOUSING</span>
    <span class="title-sub">LITERATURE REVIEW</span>
  </h1>

  <h2 class="badge badge-purpose">Purpose</h2>
  <p class="purpose-text">There are currently significant challenges in supporting displaced people with timely and equitable access to emergency and temporary accommodation and assisting them on a path to stable housing in the aftermath of a disaster. This report seeks to support agencies and decision makers to formulate and implement appropriate approaches to post-disaster housing, factoring in the scale of a disaster and varying community cohorts.</p>

  <h2 class="badge badge-recommendations">Recommendations</h2>
  <ul class="recommendation-list">
    <li>TERMINOLOGY</li>
    <li>FURTHER RESEARCH</li>
    <li>PRINCIPLES</li>
    <li>FUNDING</li>
    <li>NATIONAL PRINCIPLES</li>
    <li>CAPTURING LEARNINGS</li>
    <li>GUIDELINES</li>
    <li>PILOT PROJECT</li>
  </ul>

  <footer class="footer-band">
    <span class="footer-notch" style="left:205px"></span>
    <span class="footer-notch" style="left:398px"></span>
    <span class="contact" style="left:42px">
      <svg viewBox="0 0 18 18"><rect x="0" y="0" width="18" height="18" rx="4" fill="#fff"/><path d="M5 4 L7.5 4 L8.5 7 L7 8 C7.8 9.8 8.6 10.6 10 11 L11 9.5 L14 10.5 L14 13 C9 13.5 4.5 9 5 4 Z" fill="#1f6fd6"/></svg>
      +255 123 456 789
    </span>
    <span class="contact" style="left:252px">
      <svg viewBox="0 0 18 18"><path d="M9 1 C5.5 1 3.5 3.6 3.5 6.5 C3.5 10.5 9 17 9 17 C9 17 14.5 10.5 14.5 6.5 C14.5 3.6 12.5 1 9 1 Z" fill="#fff"/><circle cx="9" cy="6.5" r="2.2" fill="#1b4fb0"/></svg>
      Your location
    </span>
    <span class="contact" style="left:432px">
      <svg viewBox="0 0 18 18" fill="none" stroke="#fff" stroke-width="1.4"><circle cx="9" cy="9" r="7.5"/><ellipse cx="9" cy="9" rx="3.2" ry="7.5"/><line x1="1.5" y1="9" x2="16.5" y2="9"/><line x1="3" y1="5" x2="15" y2="5"/><line x1="3" y1="13" x2="15" y2="13"/></svg>
      www.examplesite.org
    </span>
  </footer>
</main>
</body>
</html>
```